Cadenza Elite Keyboard Academy is a comprehensive piano studio located in CBD area and provide individual piano lessons.

We also provide services for wedding organising band, or instrumental hiring or venue hiring, or organise concert to students.

I want my name card to be very creative, does not have to be the form or shape with the normal name card, can be in different shape. Also, I want the name card to be very upper class, because learning piano is a serious thing, so I do not want people to bargain with the prices. I want people to see it as a very elegant tuition so that they do not want to bargain and think it is worth to try.

Further more, Cadenza Elite Keyboard Academy is not like normal piano studio only provide piano lessons, we provide band services for each other event, such as cruise party, wedding etc. I want people to see it as owner of Elite Keyboard Academy, they will have different type of services all in one, I provide more than that, and I am well connected. I do not provide only piano lesson, but also all other musical knowledge and I am very professional

I want name card to be very simple, just name of company name, my name and website that's all, maybe phone number and email as well.

Please check my website to have more ideal concept.
http://harrietdowse.sitebuilder-example.com/cadenzakeyboard
Updates

Target Market(s)

For all people who love to play piano (better with upper class)

Industry/Entity Type

Wedding

Contact Information for Business Card

Harriet Dowse
Mobile:0418769052
Email: cadenzaelitekeys@mailbox-example.com

Colors

Designer to choose colors to be used in the design.

Requirements
Must have
• Creativity
Nice to have
• Black and white
some sort of piano image
Should not have
• Childish

```html
<!DOCTYPE html>
<html lang="en">
<head>
<meta charset="utf-8">
<title>Cadenza Elite Keyboard Academy — Business Card</title>
<link href="https://fonts.googleapis.com/css2?family=Josefin+Sans:wght@300;400&display=swap" rel="stylesheet">
<style>
  :root {
    --backdrop: #e9e7e4;
    --card-white: #ffffff;
    --card-black: #0d0d0d;
    --card-sheen: #2c2c2c;
    --ink: #1a1a1a;
    --ink-soft: #3a3a3a;
    --art-light: #f1f1f1;
    --art-dark: #4a4a4a;
    --logo-white: #f2f2f2;
  }
  * { box-sizing: border-box; margin: 0; padding: 0; }
  html, body {
    width: 1200px; height: 1000px; overflow: hidden;
    background: var(--backdrop);
    font-family: "Josefin Sans", sans-serif;
  }
  .canvas {
    position: relative; width: 1200px; height: 1000px;
    display: flex; align-items: center; justify-content: center; gap: 50px;
  }
  .card {
    position: relative; width: 520px; height: 300px;
    box-shadow: 0 10px 30px rgba(0,0,0,0.18);
    overflow: hidden;
  }
  /* Front: contact side */
  .card--front { background: var(--card-white); }
  .card__artwork {
    position: absolute; left: 0; top: 0; width: 230px; height: 300px;
    background: linear-gradient(180deg, var(--art-dark) 0%, var(--art-light) 65%, var(--card-white) 100%);
  }
  .card__contact {
    position: absolute; left: 250px; top: 158px; right: 14px;
    color: var(--ink);
  }
  .contact__name {
    font-size: 21px; font-weight: 400; letter-spacing: 0.5px;
    margin-bottom: 8px;
  }
  .contact__line {
    font-size: 9.2px; font-weight: 300; color: var(--ink-soft);
    line-height: 1.45; white-space: nowrap; letter-spacing: 0.2px;
  }
  /* Back: brand side */
  .card--back {
    background: radial-gradient(ellipse 60% 70% at 58% 42%, var(--card-sheen) 0%, var(--card-black) 70%);
    display: flex; flex-direction: column; align-items: center; justify-content: center;
    color: var(--logo-white);
  }
  .brand__mark {
    width: 34px; height: 34px; border: 1.5px solid var(--logo-white);
    border-radius: 50%; margin-bottom: 16px;
  }
  .brand__name {
    font-size: 26px; font-weight: 300; letter-spacing: 5px;
    text-transform: uppercase; line-height: 1;
  }
  .brand__tagline {
    display: flex; align-items: center; gap: 8px; margin-top: 6px;
    font-size: 10px; font-weight: 300; letter-spacing: 2.5px; text-transform: uppercase;
  }
  .brand__rule { width: 26px; height: 1px; background: var(--logo-white); }
</style>
</head>
<body>
<main class="canvas">
  <section class="card card--front" aria-label="Business card, contact side">
    <div class="card__artwork" role="img" aria-label="Close-up illustration of black and white piano keys"></div>
    <div class="card__contact">
      <p class="contact__name">Harriet Dowse</p>
      <p class="contact__line">mobile: 0418769052</p>
      <p class="contact__line">email: cadenzaelitekeys@mailbox-example.com</p>
      <p class="contact__line">web: harrietdowse.sitebuilder-example.com/cadenzakeyboard</p>
    </div>
  </section>

  <section class="card card--back" aria-label="Business card, brand side">
    <span class="brand__mark" aria-hidden="true"></span>
    <p class="brand__name">Cadenza Elite</p>
    <p class="brand__tagline">
      <span class="brand__rule" aria-hidden="true"></span>
      Keyboard Academy
      <span class="brand__rule" aria-hidden="true"></span>
    </p>
  </section>
</main>
</body>
</html>
```